Need a small Brochure Designing for a High Tech LED Spotlight

This is an expensive product and the best of it's kind in the world, so it needs to be marketed to intelligent, forward thinking people who appreciate and pay for excellent design and innovation. The type of people who buy Quince products i guess. It needs to be clean. The colours do not need to be in keep with our website, but our logo does need to be on the brochure. I have attached a dcoument with all the text, the order the text goes in and an idea of how i want the first page to look. All images and logos have been attached too.

Target Market(s)

This is aimed at people with high disposible incomes who spend money on the best designed products and the latest technology. The type of people who buy Quince products.

Industry/Entity Type

Product

Requirements
Must have
• The work needs to be editable by us using indesign

The pages need to be A5. I'm not sure how many pages the brochure needs to be as it does need to be clean and be spaced out well. On the file that contains the text i've indicated that 8 pages would be good.

The logos i attached - 1) Kelo Product Design Award, 2) Z Technology Award, 3) Blue Fern Design Award and 4) Keen Design Award all need to be at the bottom of the front page, quite small, but still able to see them well.

- Needs to have a QR code so that smart phones can scan the code and be taken to a pol vane clip - QR code is attached.
- Needs to have Plimbo Icon - @KestrowHomeCo
Nice to have
• Nice to remind customers on each page that the product has a 5 year Warranty and we have a 365 day Returns Policy.

```html
<!DOCTYPE html>
<html lang="en">
<head>
<meta charset="utf-8">
<title>N4 LED Spotlight Brochure</title>
<link href="https://fonts.googleapis.com/css2?family=Mulish:ital,wght@0,400;0,700;1,400&display=swap" rel="stylesheet">
<style>
:root{
  --backdrop:#c9b8a3;
  --paper:#ffffff;
  --accent:#d42a2a;
  --ink:#3a3a3a;
  --fold:#dcdcdc;
  --shadow:rgba(0,0,0,.35);
}
*{margin:0;padding:0;box-sizing:border-box}
html,body{width:1200px;height:1000px;overflow:hidden;background:var(--backdrop)}
body{font-family:"Mulish",Arial,sans-serif;color:var(--ink);position:relative}
.spread{position:absolute;left:124px;width:953px;height:336px;background:var(--paper);box-shadow:4px 5px 5px var(--shadow)}
.spread--one{top:143px}
.spread--two{top:521px}
.fold{position:absolute;left:476px;top:0;width:1px;height:100%;background:var(--fold)}
.headline{position:absolute;left:29px;top:26px;color:var(--accent);font-size:18.5px;line-height:23px;font-weight:400}
.column{position:absolute;width:134px;font-size:7.7px;line-height:9.6px;letter-spacing:.05px}
.column p{margin-bottom:9.6px}
.column em{font-style:italic}
.column strong{font-weight:700}
.section-title{color:var(--accent);font-size:10.5px;line-height:12px;font-weight:400;margin:0 0 8px}
.quote-source{text-align:right;margin-top:-9.6px}
.dimensions{border-collapse:collapse;font-size:7.7px;margin:6px 0 2px 3px}
.dimensions td,.dimensions th{font-weight:400;padding:2px 0;text-align:left}
.dimensions .fit{width:44px}
.dimensions .len{width:46px}
.footnote{font-size:4.6px;line-height:6px;margin-bottom:12px}
.photo{position:absolute}
.photo--sphere{left:791px;top:29px;width:133px;height:145px;background:linear-gradient(160deg,#8fa3a0 0%,#3f6b62 45%,#cfd3d0 100%)}
.caption{position:absolute;left:791px;top:178px;width:133px;text-align:center;font-size:7.7px}
.photo--interior{left:791px;top:0;width:162px;height:336px;background:linear-gradient(180deg,#e8d9c7 0%,#f2ede6 30%,#e3d6c4 55%,#f4f1ec 75%,#d9cdbd 100%)}
</style>
</head>
<body>

<section class="spread spread--one">
  <div class="fold"></div>
  <h1 class="headline">Simple.<br>Beautiful.<br>Intelligent.</h1>

  <div class="column" style="left:172px;top:27px">
    <p><em>'LEDs used to be prohibitively expensive, but advances in semiconductor technology mean they're now brighter and more affordable than before... it's easy to see why they're becoming so popular.'</em></p>
    <p class="quote-source">Verdict</p>
    <p>With its unrivalled performance and quality, the <strong>N4 7w</strong> is the most technologically advanced LED Spotlight in the world.</p>
    <p>Kestrow Home Co Managing Director Alan Morrow talks about the <strong>N4 7w</strong> LED Spot:</p>
    <p><em>"I've been working with the manufacturer of this exceptional product since their inception in 2008. They've received more than a hundred world patents and safety certifications so far – as far as I am concerned, there isn't an LED manufacturer in the world that comes close to their expertise and attention to detail.</em></p>
  </div>

  <div class="column" style="left:314px;top:27px">
    <p><em>Since its creation, the company has won a number of prestigious international design awards, such as the Kelo Product Design Award, the Z Technology Award, the Blue Fern Design Award, and the Keen Design Award.</em></p>
    <p><em>With high-quality, industry-leading performance, they've become the first choice for professional buyers and lighting designers in recent years. They're basically the Quince of the LED lighting industry – we're talking beautifully designed products that are miles ahead of the competition".</em></p>
    <p><em>The N4 Is The Ultimate In Lighting For The Discerning, Design Conscious And Forward Thinking Person"</em></p>
  </div>

  <div class="column" style="left:505px;top:28px">
    <h2 class="section-title">Heat Dissipation</h2>
    <p>The brightness of all LEDs deteriorates over time. Just how quickly, though, is almost exclusively down to how well the lamp can dissipate heat.</p>
    <p>Heat is the biggest enemy of the LED. Without proper heat dissipation, the critical components of any LED lamp will fail or degrade quickly. So if the LED spotlight doesn't have a well-designed, thorough heat dissipation system, the quality of light will easily degrade to an unacceptable level, with the LED simply failing very quickly.</p>
    <p>The <strong>N4 7w</strong> is crafted from the finest raw materials and uses a cutting edge heat dissipation system similar to that used to cool fuel tanks on Orbix space shuttles and brake callipers on Grand Circuit cars.</p>
    <p>This beautiful, intuitive patented design has won multiple international awards.</p>
  </div>

  <div class="column" style="left:648px;top:28px">
    <h2 class="section-title">Brightness</h2>
    <p>Brevon Manufacture the most advanced and powerful LED chips in the world. While rival companies now produce very reasonable alternatives, there's still no substitute for Brevon.</p>
    <p>The <strong>N4</strong> uses the very latest Brevon QX-4 Chip, which produces 580 warm white lumens. With 83 lumens per watt, the <strong>N4</strong> is considerably more powerful than a 50w halogen – and any other LED spot.</p>
    <p>A Lumetra LS-60 integrating sphere – a rare and very expensive piece of equipment – is used to measure the total light radiated in all directions from the lamp, giving customers a 100% accurate measurement of its so that the total power (or 'flux').</p>
  </div>

  <div class="photo photo--sphere" role="img" aria-label="Photograph of a large green integrating sphere used for light measurement"></div>
  <p class="caption">Lumetra LS-60</p>
</section>

<section class="spread spread--two">
  <div class="fold"></div>
  <h1 class="headline">Cut your<br>energy<br>consumption<br>by up to 90%.<br><br>Keep your<br>existing<br>fittings.</h1>

  <div class="column" style="left:172px;top:28px">
    <h2 class="section-title">Lifespan</h2>
    <p>As with the brightness testing on the N4, the method used to determine the lamp's lifespan of this LED Spotlight is also a highly skilled and time consuming exercise known as accelerated testing.</p>
    <p>We use an algorithm that, after around 6,000 hours of testing, calculates the number of hours remaining before the LED Lamp will start to lose a significant amount of its brightness.</p>
    <p>Tests take up to 10 months to complete, ensuring that customers get a product with real staying power.</p>
    <h2 class="section-title">Easy Installation</h2>
    <p>The N4 comes in two standard fittings: GU10 (twist and lock) and MR16 (twin pin). Installation is simple: just take your old halogens out and put the N4 in.</p>
  </div>

  <div class="column" style="left:314px;top:47px">
    <p style="margin-bottom:4px">The product Dimensions are:</p>
    <table class="dimensions">
      <tr><th class="fit"></th><th class="len">Length</th><th>Width</th></tr>
      <tr><td>GU10</td><td>60mm</td><td>50mm</td></tr>
      <tr><td>MR16</td><td>45.5mm</td><td>50mm</td></tr>
    </table>
    <p class="footnote">Please note: the dimmable N4 only comes in GU10 fitting.</p>
    <h2 class="section-title">Maintenance</h2>
    <p>With an incredible lifespan of 40,000 hours, the N4 will last for an average of over 18 years if used for six hours a day, 365 days a year. With a lifespan like this, savings on replacing failed lamps are enormous.</p>
    <h2 class="section-title">Warranty and Returns</h2>
    <p>We think the N4 is the best LED Spotlight in the world, which is why we've given it the best warranty and returns period in the world!</p>
    <p>This product comes with an</p>
  </div>

  <div class="column" style="left:505px;top:28px">
    <p>industry-leading five-year comprehensive warranty and a 365-day returns period, offering you complete security and satisfaction.</p>
    <h2 class="section-title">Colour Temperature</h2>
    <p>The N4 comes in two different colour temperatures:</p>
    <p><em>Warm White</em> – the colour we highly recommend for your home. Not quite as warm as a halogen but still retains the warm feel with a clearer light quality.</p>
    <p><em>Natural White</em> – perfect for commercial properties such as retail stores. Very clear and bright colour temperature, which helps illuminate the room to its optimum.</p>
    <h2 class="section-title">Beam Angle</h2>
    <p>The N4 is available in two different beam angles: 60 and 135 degrees.</p>
    <p>The wide beam angle of 135</p>
  </div>

  <div class="column" style="left:648px;top:28px">
    <p>degrees means this product is perfect for any well sized room. However, if you have smaller sized room or a room with a particularly high ceiling you may want to consider a narrower beam angle of 60 degrees – one of our expert team members can help you make the best decision for your property.</p>
  </div>

  <div class="photo photo--interior" role="img" aria-label="Photograph of a bright modern interior with a pendant lamp over a white kitchen counter"></div>
</section>

</body>
</html>
```